Flooring & Interior Design showroom

Just bought this business- Kestrel Lane Flooring & Interiors. Love our logo (we are on Kestrel Lane )and colors
Forest green, gold and black
Love that the back lists everything we do. We no longer have plenotilex but need to add in LVP/ SPC and need to take out vantor shadehub logo at the bottom and use the quib logo instead (maybe? open to suggestions)

Not in love with our cards- I want a higher end look
I hate the gradient poop color we have now.
Would love if they were all black - maybe or ??
or had a foil or embossing?

```html
<!DOCTYPE html>
<html lang="en">
<head>
<meta charset="utf-8">
<title>Kestrel Lane Flooring &amp; Interiors – Business Card</title>
<link href="https://fonts.googleapis.com/css2?family=Montserrat:wght@400;500;600&display=swap" rel="stylesheet">
<style>
  :root {
    --backdrop: #a7a7a7;
    --card: #151515;
    --forest: #4f8a5b;
    --copper: #9b705d;
    --gold: #e4d699;
    --ink: #f2f2f2;
  }
  * { box-sizing: border-box; margin: 0; padding: 0; }
  html, body { width: 900px; height: 1200px; overflow: hidden; }
  body {
    position: relative;
    background: var(--backdrop);
    font-family: "Montserrat", Arial, sans-serif;
    color: var(--ink);
  }
  .card {
    position: absolute;
    left: 80px;
    width: 742px;
    height: 441px;
    background: var(--card);
    box-shadow: 0 3px 10px rgba(0,0,0,.35);
    overflow: hidden;
  }
  .card--front { top: 131px; }
  .card--back { top: 638px; height: 440px; }

  /* wordmark */
  .wordmark { position: absolute; color: var(--gold); font-weight: 500; line-height: 1.1; }
  .wordmark__name { display: block; letter-spacing: .02em; }
  .wordmark__tag { display: block; letter-spacing: .08em; text-transform: uppercase; }
  .card--front .wordmark { left: 44px; top: 86px; }
  .card--front .wordmark__name { font-size: 34px; }
  .card--front .wordmark__tag { font-size: 14px; margin-top: 8px; }
  .card--back .wordmark { left: 0; right: 0; top: 92px; text-align: center; }
  .card--back .wordmark__name { font-size: 56px; }
  .card--back .wordmark__tag { font-size: 22px; margin-top: 12px; }

  /* front */
  .person { position: absolute; right: 39px; top: 44px; text-align: right; }
  .person__name { font-size: 24px; font-weight: 600; color: var(--forest); letter-spacing: .02em; }
  .person__role { font-size: 15px; margin-top: 1px; }
  .accent-bar { position: absolute; right: 0; top: 52px; width: 16px; height: 38px; background: var(--forest); }

  .contacts { position: absolute; left: 48px; top: 251px; list-style: none; }
  .contacts li { display: flex; align-items: center; height: 25px; font-size: 16px; }
  .contacts svg { width: 14px; height: 14px; margin-right: 13px; fill: var(--forest); flex: none; }

  .address { position: absolute; right: 39px; top: 332px; text-align: right; font-size: 16px; line-height: 21px; }
  .swoosh { position: absolute; left: 0; bottom: 0; width: 742px; height: 60px; }
  .license { position: absolute; right: 39px; bottom: 10px; font-size: 16px; }

  /* back */
  .services {
    position: absolute; top: 296px; left: 48px; right: 30px;
    display: grid; grid-template-columns: 258px 232px 1fr;
  }
  .services ul { list-style: none; }
  .services li { font-size: 17px; line-height: 19.7px; display: flex; align-items: center; }
  .services li::before {
    content: ""; width: 6px; height: 6px; border-radius: 50%;
    background: var(--forest); margin-right: 12px;
  }
</style>
</head>
<body>

<section class="card card--front">
  <div class="wordmark">
    <span class="wordmark__name">Kestrel Lane</span>
    <span class="wordmark__tag">Flooring &amp; Interiors</span>
  </div>

  <div class="person">
    <p class="person__name">Mara Whitlow</p>
    <p class="person__role">Owner/ Designer</p>
  </div>
  <div class="accent-bar"></div>

  <ul class="contacts">
    <li><svg viewBox="0 0 16 16"><path d="M2 6c0-2 2-3 6-3s6 1 6 3v1h-3V6H5v1H2zM4 8h8l2 5H2z"/></svg>(555) 372-0148</li>
    <li><svg viewBox="0 0 16 16"><path d="M4 0h8v16H4zM5.5 2v10h5V2z"/></svg>555-876-0193</li>
    <li><svg viewBox="0 0 16 16"><path d="M1 5h14v10H1zM4 1h6v3H4zM3 8h4v2H3z"/></svg>555.647. 0177</li>
    <li><svg viewBox="0 0 16 16"><path d="M1 4h14v2L8 10 1 6zM1 8l7 4 7-4v5H1z"/></svg>info@kestrellaneflooring.com</li>
    <li><svg viewBox="0 0 16 16"><circle cx="8" cy="8" r="6.5"/></svg>www.kestrellaneflooring.com</li>
  </ul>

  <p class="address">314 Kestrel Ln<br>Cedar Hollow, CA 90417</p>

  <svg class="swoosh" viewBox="0 0 742 60" preserveAspectRatio="none" aria-hidden="true">
    <path d="M8 60 C150 22 360 8 520 8 C360 14 200 30 120 60 Z" fill="var(--copper)"/>
    <path d="M130 60 C240 34 380 18 470 17 L742 17 L742 60 Z" fill="var(--forest)"/>
  </svg>
  <p class="license">CA Lic # 612047</p>
</section>

<section class="card card--back">
  <div class="wordmark">
    <span class="wordmark__name">Kestrel Lane</span>
    <span class="wordmark__tag">Flooring &amp; Interiors</span>
  </div>

  <div class="services">
    <ul>
      <li>Area rugs</li><li>Hardwood</li><li>Cork</li><li>Bamboo</li><li>Laminate</li><li>Vinyl</li>
    </ul>
    <ul>
      <li>Shades</li><li>Sheers</li><li>Shutters</li><li>Drapes</li><li>Bedding</li><li>Upholstery</li>
    </ul>
    <ul>
      <li>Blinds</li><li>Carpet</li><li>verticals</li><li>Bed spreads</li><li>Fabric</li><li>valances</li>
    </ul>
  </div>
</section>

</body>
</html>
```